New Flyer Design Project

I would like to purchase a customized version of a design you have previously submitted - https://www.brivomart.example/design/58204731

I want this to be something that looks really good.
We use this to explain our service agreements.
our website is www.plorvex.example I want to stick with those colors.

```html
<!DOCTYPE html>
<html lang="en">
<head>
<meta charset="utf-8">
<title>Plorvex Support Plans</title>
<link href="https://fonts.googleapis.com/css2?family=Montserrat:wght@400;500;700;800&display=swap" rel="stylesheet">
<style>
  :root {
    --brand-red: #93272a;
    --brand-gray: #6d6e71;
    --ink-dark: #58595b;
    --paper: #ffffff;
    --backdrop: #e9e9ea;
    --row-line: #76777a;
  }
  * { box-sizing: border-box; margin: 0; padding: 0; }
  html, body { width: 1200px; height: 1200px; overflow: hidden; background: var(--backdrop); }
  body { font-family: "Montserrat", sans-serif; position: relative; }

  .flyer {
    position: absolute; left: 0; top: 172px;
    width: 1200px; height: 856px;
    background: var(--paper);
    overflow: hidden;
  }
  .flyer-shapes { position: absolute; inset: 0; }

  .brand {
    position: absolute; left: 30px; top: 70px;
    display: flex; align-items: center; gap: 12px;
  }
  .brand-mark { width: 22px; height: 22px; background: var(--brand-red); }
  .brand-name { font-weight: 700; font-size: 50px; color: var(--ink-dark); letter-spacing: 1px; }

  .title {
    position: absolute; right: 26px; top: 55px; height: 85px;
    display: flex; align-items: center;
    font-weight: 700; font-size: 46px; color: var(--paper); white-space: nowrap;
  }

  .services-label {
    position: absolute; left: 114px; width: 446px; top: 230px;
    text-align: center; font-weight: 700; font-size: 42px; color: var(--paper);
  }

  .plan-head {
    position: absolute; top: 222px; text-align: center; color: var(--paper);
  }
  .plan-head .plan-name {
    font-weight: 800; font-size: 25px; line-height: 1.1;
    text-shadow: -1.5px -1.5px 0 var(--brand-gray), 1.5px -1.5px 0 var(--brand-gray),
                 -1.5px 1.5px 0 var(--brand-gray), 1.5px 1.5px 0 var(--brand-gray);
  }
  .plan-head .plan-price { font-weight: 800; font-size: 34px; line-height: 1.25; }
  .plan-head .per-unit { font-weight: 500; font-size: 22px; }
  .plan-security { left: 575px; width: 250px; }
  .plan-essentials { left: 825px; width: 259px; }

  .service-table {
    position: absolute; left: 129px; top: 300px; width: 940px;
    list-style: none;
  }
  .service-row {
    display: grid; grid-template-columns: 431px 265px 244px;
    height: 26.6px; align-items: center;
    border-bottom: 1.3px solid var(--row-line);
    color: var(--paper); font-size: 14.2px;
  }
  .service-row:last-child { border-bottom: none; }
  .service-name { display: flex; align-items: center; gap: 12px; padding-left: 8px; white-space: nowrap; }
  .service-name::before {
    content: ""; width: 5px; height: 5px; border-radius: 50%; background: var(--paper); flex: none;
  }
  .cell { text-align: center; display: flex; justify-content: center; align-items: center; height: 100%; border-left: 1.3px solid var(--row-line); font-size: 14.2px; }
  .cell.col-essentials { padding-right: 6px; }
  .tick { width: 16px; height: 16px; }
</style>
</head>
<body>
<main class="flyer">
  <svg class="flyer-shapes" width="1200" height="856" viewBox="0 0 1200 856" aria-hidden="true">
    <path d="M606 55 H1200 V140 H567 Q560 140 564 133 Z" fill="var(--brand-gray)"/>
    <rect x="114" y="184" width="972" height="627" rx="20" fill="var(--brand-gray)"/>
    <path d="M616 214 H1084 V300 H560 Z" fill="var(--brand-red)"/>
    <rect x="114" y="300" width="970" height="483" fill="var(--brand-red)"/>
    <line x1="560" y1="300" x2="616" y2="214" stroke="var(--paper)" stroke-width="1.5"/>
    <line x1="616" y1="214" x2="1084" y2="214" stroke="var(--paper)" stroke-width="1.5"/>
    <line x1="560" y1="300" x2="1084" y2="300" stroke="var(--paper)" stroke-width="1.5"/>
    <line x1="114" y1="783" x2="1084" y2="783" stroke="var(--paper)" stroke-width="1.5"/>
    <line x1="825" y1="228" x2="825" y2="300" stroke="var(--row-line)" stroke-width="1.3"/>
    <symbol id="tick" viewBox="0 0 16 16">
      <circle cx="8" cy="8" r="7.4" fill="none" stroke="#fff" stroke-width="1.2"/>
      <circle cx="8" cy="8" r="6" fill="#fff"/>
      <path d="M4.6 8.2 L7 10.5 L11.4 5.6" fill="none" stroke="#93272a" stroke-width="1.8" stroke-linecap="round" stroke-linejoin="round"/>
    </symbol>
  </svg>

  <div class="brand">
    <span class="brand-name">Plorvex</span>
    <span class="brand-mark"></span>
  </div>

  <h1 class="title">Plorvex Support Plans</h1>

  <div class="services-label">Services</div>

  <div class="plan-head plan-security">
    <div class="plan-name">Security Plus</div>
    <div class="plan-price">$75.00</div>
  </div>
  <div class="plan-head plan-essentials">
    <div class="plan-name">IT Essentials</div>
    <div class="plan-price">$55.00 <span class="per-unit">Per Pc</span></div>
  </div>

  <ul class="service-table">
    <li class="service-row"><span class="service-name">Unlimited US bases Remote Help Desk Support</span><span class="cell"><svg class="tick"><use href="#tick"/></svg></span><span class="cell col-essentials"><svg class="tick"><use href="#tick"/></svg></span></li>
    <li class="service-row"><span class="service-name">Unlimited On-Site Support</span><span class="cell"><svg class="tick"><use href="#tick"/></svg></span><span class="cell col-essentials">Available</span></li>
    <li class="service-row"><span class="service-name">Advanced Cybersecurity and Threat Hunting</span><span class="cell"><svg class="tick"><use href="#tick"/></svg></span><span class="cell col-essentials">Available</span></li>
    <li class="service-row"><span class="service-name">Managed Antivirus Protection</span><span class="cell"><svg class="tick"><use href="#tick"/></svg></span><span class="cell col-essentials"><svg class="tick"><use href="#tick"/></svg></span></li>
    <li class="service-row"><span class="service-name">Multifactor Authentication Powered by Keyvara</span><span class="cell"><svg class="tick"><use href="#tick"/></svg></span><span class="cell col-essentials">Available</span></li>
    <li class="service-row"><span class="service-name">Cyber Security Awareness Training</span><span class="cell"><svg class="tick"><use href="#tick"/></svg></span><span class="cell col-essentials">Available</span></li>
    <li class="service-row"><span class="service-name">Enhanced Span Filtering</span><span class="cell"><svg class="tick"><use href="#tick"/></svg></span><span class="cell col-essentials">Available</span></li>
    <li class="service-row"><span class="service-name">Internet Content Filtering</span><span class="cell"><svg class="tick"><use href="#tick"/></svg></span><span class="cell col-essentials">Available</span></li>
    <li class="service-row"><span class="service-name">Proactive Security and System Monitoring</span><span class="cell"><svg class="tick"><use href="#tick"/></svg></span><span class="cell col-essentials"><svg class="tick"><use href="#tick"/></svg></span></li>
    <li class="service-row"><span class="service-name">Security and Vulnerability patching</span><span class="cell"><svg class="tick"><use href="#tick"/></svg></span><span class="cell col-essentials"><svg class="tick"><use href="#tick"/></svg></span></li>
    <li class="service-row"><span class="service-name">Backup and disaster recovery</span><span class="cell"><svg class="tick"><use href="#tick"/></svg></span><span class="cell col-essentials"><svg class="tick"><use href="#tick"/></svg></span></li>
    <li class="service-row"><span class="service-name">Network Management and Administration</span><span class="cell"><svg class="tick"><use href="#tick"/></svg></span><span class="cell col-essentials"><svg class="tick"><use href="#tick"/></svg></span></li>
    <li class="service-row"><span class="service-name">Vantrel Office Suite Administration and Configuration</span><span class="cell"><svg class="tick"><use href="#tick"/></svg></span><span class="cell col-essentials"><svg class="tick"><use href="#tick"/></svg></span></li>
    <li class="service-row"><span class="service-name">Vantrel Cloud Administration and Configuration</span><span class="cell"><svg class="tick"><use href="#tick"/></svg></span><span class="cell col-essentials"><svg class="tick"><use href="#tick"/></svg></span></li>
    <li class="service-row"><span class="service-name">Vantrel OS and Server Support</span><span class="cell"><svg class="tick"><use href="#tick"/></svg></span><span class="cell col-essentials"><svg class="tick"><use href="#tick"/></svg></span></li>
    <li class="service-row"><span class="service-name">Managed DNS</span><span class="cell"><svg class="tick"><use href="#tick"/></svg></span><span class="cell col-essentials"><svg class="tick"><use href="#tick"/></svg></span></li>
    <li class="service-row"><span class="service-name">Hardware and Software Procurement</span><span class="cell"><svg class="tick"><use href="#tick"/></svg></span><span class="cell col-essentials"><svg class="tick"><use href="#tick"/></svg></span></li>
    <li class="service-row"><span class="service-name">Asset Management</span><span class="cell"><svg class="tick"><use href="#tick"/></svg></span><span class="cell col-essentials"><svg class="tick"><use href="#tick"/></svg></span></li>
  </ul>
</main>
</body>
</html>
```